DOG DAYCARE BILLBOARD

Design a bold exciting billboard that can be read easily from a distance! Our goal is brand awareness and showcasing the services we offer (Boarding, Grooming, Daycare, and Training.
we would like to see examples with the phrase "your best friend's best day". Our name Bright Meadow Canine Activity Center (or just Bright Meadow might work better and could be bigger) and the services we provide.
(there are two examples of what we like included in the pictures)
you can find more information o our website at pawplayhouse@mailbox-example.com.

```html
<!DOCTYPE html>
<html lang="en">
<head>
<meta charset="utf-8">
<title>Bright Meadow Billboard</title>
<link rel="stylesheet" href="https://fonts.googleapis.com/css2?family=Montserrat:wght@800;900&display=swap">
<style>
  :root {
    --page-bg: #ececec;
    --sign-yellow: #e4c43a;
    --sign-yellow-light: #ecd260;
    --ink: #111111;
    --photo-light: #f4f1ea;
    --photo-mid: #e3dccd;
  }
  * { margin: 0; padding: 0; box-sizing: border-box; }
  html, body {
    width: 1200px;
    height: 903px;
    overflow: hidden;
    background: var(--page-bg);
  }
  .billboard {
    position: absolute;
    left: 20px;
    top: 171px;
    width: 1160px;
    height: 560px;
    background: var(--sign-yellow);
    overflow: hidden;
    font-family: "Montserrat", sans-serif;
    color: var(--ink);
  }
  .billboard__waves {
    position: absolute;
    inset: 0;
    width: 100%;
    height: 100%;
  }
  .headline {
    position: absolute;
    left: 72px;
    top: 104px;
    text-transform: uppercase;
    font-weight: 900;
    line-height: 1;
  }
  .headline__lead {
    display: block;
    font-size: 50px;
    letter-spacing: 0.5px;
  }
  .headline__main {
    display: block;
    font-size: 114px;
    letter-spacing: -3px;
    margin-top: 2px;
  }
  .services-band {
    position: absolute;
    left: 0;
    top: 0;
    width: 100%;
    height: 100%;
  }
  .services {
    position: absolute;
    left: 72px;
    top: 322px;
    display: grid;
    grid-template-columns: 315px 300px;
    row-gap: 20px;
    list-style: none;
  }
  .services__item {
    display: flex;
    align-items: center;
    gap: 11px;
    color: var(--sign-yellow);
    font-weight: 800;
    font-size: 35px;
    line-height: 1;
    text-transform: uppercase;
    letter-spacing: -0.5px;
  }
  .services__tick { width: 38px; height: 38px; flex: none; }
  .brand-name {
    position: absolute;
    left: 60px;
    width: 640px;
    top: 472px;
    text-align: center;
    font-weight: 900;
    font-size: 42px;
    letter-spacing: 3px;
    text-transform: uppercase;
  }
  .dog-photo {
    position: absolute;
    left: 742px;
    top: 28px;
    width: 418px;
    height: 532px;
    border-radius: 170px 170px 0 0;
    background: radial-gradient(ellipse at 50% 40%, var(--photo-light) 0%, var(--photo-mid) 100%);
  }
</style>
</head>
<body>
  <section class="billboard">
    <svg class="billboard__waves" viewBox="0 0 1160 560" aria-hidden="true">
      <path d="M0 40 C260 10 520 120 760 60 S1080 0 1160 30 L1160 0 L0 0 Z" fill="var(--sign-yellow-light)" opacity="0.5"/>
      <path d="M0 260 C240 200 520 240 760 150 L760 230 C520 300 260 260 0 300 Z" fill="var(--sign-yellow-light)" opacity="0.35"/>
    </svg>

    <h1 class="headline">
      <span class="headline__lead">Your best friend's</span>
      <span class="headline__main">Best day</span>
    </h1>

    <svg class="services-band" viewBox="0 0 1160 560" aria-hidden="true">
      <polygon points="0,300 790,290 740,436 0,440" fill="var(--ink)"/>
    </svg>

    <ul class="services">
      <li class="services__item">
        <svg class="services__tick" viewBox="0 0 42 42" aria-hidden="true"><rect x="4" y="6" width="32" height="32" rx="5" fill="none" stroke="var(--sign-yellow)" stroke-width="4"/><path d="M11 21 L19 29 L37 6" fill="none" stroke="var(--sign-yellow)" stroke-width="6" stroke-linecap="round" stroke-linejoin="round"/></svg>
        Boarding
      </li>
      <li class="services__item">
        <svg class="services__tick" viewBox="0 0 42 42" aria-hidden="true"><rect x="4" y="6" width="32" height="32" rx="5" fill="none" stroke="var(--sign-yellow)" stroke-width="4"/><path d="M11 21 L19 29 L37 6" fill="none" stroke="var(--sign-yellow)" stroke-width="6" stroke-linecap="round" stroke-linejoin="round"/></svg>
        Grooming
      </li>
      <li class="services__item">
        <svg class="services__tick" viewBox="0 0 42 42" aria-hidden="true"><rect x="4" y="6" width="32" height="32" rx="5" fill="none" stroke="var(--sign-yellow)" stroke-width="4"/><path d="M11 21 L19 29 L37 6" fill="none" stroke="var(--sign-yellow)" stroke-width="6" stroke-linecap="round" stroke-linejoin="round"/></svg>
        Daycare
      </li>
      <li class="services__item">
        <svg class="services__tick" viewBox="0 0 42 42" aria-hidden="true"><rect x="4" y="6" width="32" height="32" rx="5" fill="none" stroke="var(--sign-yellow)" stroke-width="4"/><path d="M11 21 L19 29 L37 6" fill="none" stroke="var(--sign-yellow)" stroke-width="6" stroke-linecap="round" stroke-linejoin="round"/></svg>
        Training
      </li>
    </ul>

    <p class="brand-name">Bright Meadow</p>

    <div class="dog-photo" role="img" aria-label="Photo of a happy white bulldog with its tongue out"></div>
  </section>
</body>
</html>
```